Rediscover Your Inner Artist

Our organization is launching a new art workshop series in Seaside, Florida, where our Institute is based. We are building a new academic village there and these first four spring courses will be our inaugural event. I have a website developed for these programs at www.brambleridgelearningglen.com.

Now, I need a poster so that I can start marketing our programs in the town and elsewhere. It would be nice to promote all four of the programs on one poster due to expense, however, I think it might make sense to have each program have its own poster. If it was divided into four different posters, it might be nice to be able to use the poster image on 3.5 X 8.5" card stock so that they can be distributed in shops in town.
Updates

I have updated my logo file at a higher resolution per a request by one of the designers.  Please use this version.

Thank you!

Marta

I probably should have been more specific about the poster size.  I'm thinking approx. 18 X 24 and the image should be vertical. 

Target Market(s)

18 years and up. I'm thinking the people who attend are empty nester types mostly.

Industry/Entity Type

Marketing

Requirements
Must have
• The name of the four programs with dates.
Location of the programs.
Institute logo and name.

```html
<!DOCTYPE html>
<html lang="en">
<head>
<meta charset="utf-8">
<title>Art Workshop Series – Rediscover Your Inner Artist</title>
<link rel="stylesheet" href="https://fonts.googleapis.com/css2?family=Bebas+Neue&family=Oswald:wght@400;500&family=Teko:wght@400;500&display=swap">
<style>
  :root {
    --bg-light: #f4f4f5;
    --bg-mid: #d9dadc;
    --bg-edge: #c4c5c8;
    --ink-grey: #4a4d52;
    --ink-dark: #2f3237;
    --accent-red: #c8171d;
    --accent-red-dark: #8e1014;
    --silver-top: #ffffff;
    --silver-bottom: #b9bbbf;
    --frame: #ffffff;
    --rule: #9a9ca0;
  }
  * { margin: 0; padding: 0; box-sizing: border-box; }
  html, body { width: 800px; height: 1200px; overflow: hidden; }
  body {
    position: relative;
    background:
      radial-gradient(circle at 18% 8%, rgba(255,255,255,.55) 0 34px, transparent 36px),
      radial-gradient(circle at 84% 14%, rgba(255,255,255,.45) 0 48px, transparent 50px),
      radial-gradient(circle at 92% 46%, rgba(255,255,255,.4) 0 40px, transparent 42px),
      radial-gradient(circle at 8% 58%, rgba(255,255,255,.35) 0 44px, transparent 46px),
      radial-gradient(circle at 70% 26%, rgba(255,255,255,.35) 0 28px, transparent 30px),
      radial-gradient(ellipse at 50% 45%, var(--bg-light) 0%, var(--bg-mid) 70%, var(--bg-edge) 100%);
    font-family: "Bebas Neue", "Oswald", sans-serif;
    color: var(--ink-grey);
  }
  header p, header h1, header h2, .meta, .disciplines, .cta, .web { white-space: nowrap; }
  .institute {
    position: absolute; top: 28px; left: 0; width: 100%;
    text-align: center; font-family: "Oswald", sans-serif; font-weight: 500;
    font-size: 20px; letter-spacing: 1px; color: var(--ink-grey);
  }
  .title {
    position: absolute; top: 92px; left: 0; width: 100%;
    text-align: center; font-family: "Teko", sans-serif; font-weight: 400;
    font-size: 104px; line-height: 1; letter-spacing: 0;
    background: linear-gradient(180deg, var(--silver-top) 15%, var(--silver-bottom) 85%);
    -webkit-background-clip: text; background-clip: text; color: transparent;
    filter: drop-shadow(0 2px 2px rgba(0,0,0,.35));
  }
  .tagline {
    position: absolute; top: 216px; left: 0; width: 100%;
    text-align: center; font-family: "Bebas Neue", sans-serif;
    font-size: 70px; line-height: 1; letter-spacing: 1px;
    color: var(--accent-red);
    text-shadow: 0 2px 2px rgba(0,0,0,.25);
  }
  .meta {
    position: absolute; top: 366px; font-family: "Bebas Neue", sans-serif;
    font-size: 42px; line-height: 1; letter-spacing: .5px; color: var(--ink-grey);
  }
  .meta em { font-style: normal; color: var(--accent-red); }
  .meta-date { left: 77px; }
  .meta-place { right: 27px; }
  .photo {
    position: absolute; border: 8px solid var(--frame);
    box-shadow: 0 3px 10px rgba(0,0,0,.35);
  }
  .photo-one   { left: 43px;  top: 451px; width: 240px; height: 373px; background: linear-gradient(160deg, #b9c6d2, #8a7f76 60%, #3b3432); }
  .photo-three { left: 343px; top: 451px; width: 240px; height: 365px; background: linear-gradient(170deg, #e8e6e2, #9b8a7f 45%, #5d6270); }
  .photo-two   { left: 183px; top: 567px; width: 241px; height: 369px; background: linear-gradient(170deg, #c7c3be, #a07a62 50%, #2b6f8c 80%); }
  .photo-four  { left: 516px; top: 564px; width: 240px; height: 369px; background: linear-gradient(165deg, #a57662, #c9bfb4 45%, #3b3f4a); }
  .age {
    position: absolute; left: 43px; top: 852px; display: flex; align-items: center; gap: 8px;
    font-family: "Bebas Neue", sans-serif; font-size: 36px; color: var(--ink-grey);
  }
  .age-badge {
    width: 64px; height: 64px; border-radius: 50%;
    background: radial-gradient(circle at 40% 35%, var(--accent-red), var(--accent-red-dark));
    border: 3px solid #fff; box-shadow: 0 2px 5px rgba(0,0,0,.35);
    color: #fff; font-size: 32px; display: flex; align-items: center; justify-content: center;
  }
  .disciplines {
    position: absolute; top: 983px; left: 64px; width: 672px; height: 70px;
    border-top: 1px solid var(--rule); border-bottom: 1px solid var(--rule);
    display: flex; align-items: center; justify-content: center;
    font-family: "Bebas Neue", sans-serif; font-size: 45px; letter-spacing: .3px;
    color: var(--accent-red);
  }
  .disciplines .sep { color: var(--accent-red); margin: 0 7px; }
  .cta {
    position: absolute; top: 1074px; left: 0; width: 100%; text-align: center;
    font-family: "Bebas Neue", sans-serif; font-size: 41px; color: var(--ink-dark);
  }
  .web {
    position: absolute; top: 1132px; left: 0; width: 100%; text-align: center;
    font-family: "Bebas Neue", sans-serif; font-size: 31px; letter-spacing: .5px; color: var(--ink-dark);
  }
</style>
</head>
<body>
  <header>
    <p class="institute">THE BRAMBLE RIDGE INSTITUTE</p>
    <h1 class="title">ART WORKSHOP SERIES</h1>
    <h2 class="tagline">REDISCOVER YOUR INNER ARTIST</h2>
  </header>

  <p class="meta meta-date">DATE | <em>MAY &amp; JUNE</em></p>
  <p class="meta meta-place">SEASIDE | <em>FLORIDA</em></p>

  <div class="photo photo-one" role="img" aria-label="Photography instructor holding a camera by the sea"></div>
  <div class="photo photo-three" role="img" aria-label="Design instructor smiling under a studio umbrella"></div>
  <div class="photo photo-two" role="img" aria-label="Painting instructor portrait"></div>
  <div class="photo photo-four" role="img" aria-label="Drawing instructors, a smiling couple outdoors"></div>

  <div class="age">AGE: <span class="age-badge">18+</span></div>

  <p class="disciplines">PHOTOGRAPHY<span class="sep">|</span>DESIGN<span class="sep">|</span>PAINTING<span class="sep">|</span>DRAWING</p>

  <p class="cta">VISIT OUR WEBSITE AND REGISTER ONLINE</p>
  <p class="web">WWW.BRAMBLERIDGELEARNINGGLEN.COM/</p>
</body>
</html>
```